BRQ Company Introduction Presentation for Industrial Electronics and Automation

We are established since 2011 and we have 50 employees. We have two divisions in our company in Industrial Electronics Repair and Automation Solutions. We would like to make a presentation for those two sectors in our company.

BRQ COMPANY provides Industrial Electronics Repairs and Supplies as well as Automation Solutions.
Industrial Electronics: We repair and supply all kind of Industrial Electronic equipment including: PLCs, Drives, Servo Drives, Invertor, HMIs, Controllers .. Etc.
Automation Solutions: Provide Automation Solutions & Services.

We have several presentations attached for your guideline and you can use the material and wording in needed.
We are present in 3 countries: Kuwait, Saudi, UAE with 5 offices. I have attached some material that can help in the presentation.
Our customers:
Factories: F&B, Steel, Packing, Paper, Chemical, Glass
Services Companies: O&M, Transport, Marine
Electricity – Water – Wastewater: PAV, DRH
Oil & Gas (Government & Private: GWTR, Olvar, BZA, HRF
Building Management Systems: Malls, Commercial Buildings, Stadium

What items do we repair & Supply?
Power Supplies, Secondary DC Supplies, Processor Cards, Memory Cards, Interface Modules, Analog I/O Cards, Digital I/O Cards, Communication Cards, Remote I/O, Distribution Panel, Program Loaders, PCB (Boards).
Operation Panels, Servo Drives, Servo Motors, Axis cards, Processor Cards, Memory Cards.
All Servo Drives & Motors, Transducers, Interface Cards.
Wire Feeders, Weld Timers.
Industrial Monitors, Message/Status Display, Operator Interfaces .
Robot Arms

What are the added values of brq?
QFP - QUALITY / Fast / Price

Target Market(s)

Industrial Factories, Energy, Water, Wastewater and Oil & Gas.

Colors
86cae7
0692cd

Requirements
Must have
• - Vission, mission, goal
- Our journey
- services
- clients (Kuwait & Saudi)
- Major brands,
- facility
- certification
- automation projects
- contact details for 3 countries
Nice to have
• other things
Should not have
• nothing in mind

```html
<!DOCTYPE html>
<html lang="en">
<head>
<meta charset="utf-8">
<title>BRQ Company Introduction Presentation</title>
<link href="https://fonts.googleapis.com/css2?family=Roboto:wght@300;400;500;700&display=swap" rel="stylesheet">
<style>
:root{
  --blue:#0692cd;
  --sky:#86cae7;
  --pill:#dde9f4;
  --ink:#3f4750;
  --muted:#6a747e;
  --rule:#b9dcef;
  --page:#ffffff;
}
*{margin:0;padding:0;box-sizing:border-box}
html,body{width:900px;height:1200px;overflow:hidden;background:var(--page)}
body{position:relative;font-family:'Roboto',Arial,sans-serif;color:var(--ink)}
.slide{position:absolute;width:313px;height:176px;background:#fff;overflow:hidden;box-shadow:0 6px 14px rgba(0,0,0,.22)}
.abs{position:absolute}
.slide-title{position:absolute;left:13px;top:7px;font-size:11.5px;font-weight:400;color:var(--blue);letter-spacing:.6px;white-space:nowrap}
.slide-title.spaced{letter-spacing:4.5px}
.title-rule{position:absolute;left:10px;right:10px;top:23px;height:1px;background:var(--rule)}
.brand{position:absolute;display:flex;align-items:center;gap:3px;color:var(--blue);font-weight:700;white-space:nowrap}
.brand .mark{background:var(--blue);display:block}
.brand-small{left:252px;top:6px;font-size:10px}
.brand-small .mark{width:10px;height:10px}
.footer{position:absolute;left:15px;top:163px;font-size:6.5px;color:var(--ink)}
.page-no{position:absolute;right:9px;top:163px;font-size:6px;color:var(--muted);padding-left:5px;border-left:1px solid #ddd}
.photo{position:absolute;border-radius:9px}
/* cover */
.cover-tag{position:absolute;left:48px;top:85px;font-size:4.6px;color:var(--sky);letter-spacing:.3px}
.cover-title{position:absolute;left:17px;top:92px;font-size:14px;color:var(--blue);font-weight:400}
.cover-sub{position:absolute;left:17px;top:112px;font-size:5px;color:var(--blue);letter-spacing:.6px;line-height:7.5px}
/* agenda */
.agenda-item{position:absolute;width:120px;height:29px;background:var(--pill);border-radius:10px 0 10px 0;padding:4px 6px 0 19px}
.agenda-num{position:absolute;width:24px;height:24px;border-radius:50%;background:var(--blue);border:2px solid #fff;box-shadow:0 1px 3px rgba(0,0,0,.35);color:#fff;font-size:9px;display:flex;align-items:center;justify-content:center}
.agenda-item h3{font-size:5px;font-weight:400;color:var(--blue);letter-spacing:.5px;margin-bottom:2px}
.agenda-item p{font-size:3.6px;color:var(--muted);line-height:4.6px}
/* vision */
.vm-block{position:absolute;left:106px;width:200px}
.vm-block h3{font-size:6.5px;font-weight:400;color:var(--blue);letter-spacing:.8px;margin-bottom:2px}
.vm-block p{font-size:5.4px;line-height:8px;color:var(--ink)}
/* journey */
.year{position:absolute;font-size:6.5px;color:#222;line-height:7px}
.year small{display:block;font-size:3.8px;line-height:4.3px;color:#444}
.journey-note{position:absolute;left:122px;top:43px;width:175px;font-size:5.6px;line-height:7px;color:var(--blue);text-align:justify}
.brand-large{left:176px;top:74px;font-size:30px;gap:4px}
.brand-large .mark{width:36px;height:36px}
.brand-large-tag{position:absolute;left:218px;top:110px;font-size:5.6px;color:var(--blue);letter-spacing:.2px}
/* services hub */
.hub-pill{position:absolute;left:161px;width:103px;height:17px;border-radius:8px 0 8px 0;background:rgba(210,225,232,.35);border:1px solid rgba(255,255,255,.25);color:rgba(255,255,255,.85);font-size:6.2px;letter-spacing:1px;line-height:7.6px;padding:1px 0 0 13px}
.hub-footer{color:#fff}
/* service cards */
.card-head{position:absolute;font-size:6.5px;color:var(--blue);letter-spacing:.3px;white-space:nowrap}
.card-list{position:absolute;font-size:3.9px;color:var(--muted);list-style:none;line-height:7.3px;white-space:nowrap}
.card-list li span{display:inline-block;width:10px;text-align:right;margin-right:4px}
.repair-title{position:absolute;left:168px;top:44px;font-size:8.5px;letter-spacing:1.6px;color:var(--ink);line-height:9.8px;font-weight:300}
.repair-list{position:absolute;left:168px;top:68px;font-size:5.6px;line-height:7.3px;color:var(--ink);list-style:none}
.energy-title{position:absolute;left:22px;top:35px;font-size:8px;letter-spacing:2.2px;color:var(--blue);line-height:9.2px}
.energy-title small{font-size:6px;letter-spacing:1.6px}
.energy-list{position:absolute;left:22px;top:87px;list-style:none;font-size:5px;line-height:12.5px;color:var(--ink)}
/* clients */
.client{position:absolute;transform:translateX(-50%);font-size:5px;font-weight:500;color:#355b7a;white-space:nowrap;text-align:center;display:flex;align-items:center;gap:2px}
.client i{display:block;width:5px;height:5px;border-radius:50%;background:var(--blue)}
/* certificates */
.cert{position:absolute;top:31px;width:70px;height:125px;background:#f4f6f8;border:1px solid #d6dbe0}
.cert .sheet{position:absolute;left:4px;top:3px;right:4px;height:96px;background:#fff;box-shadow:0 0 2px rgba(0,0,0,.15)}
.cert .sheet b{position:absolute;left:6px;right:6px;height:1px;background:#cfd4d9}
.cert .seal{position:absolute;width:10px;height:10px;border-radius:50%;border:1px solid #9fb3c8;left:8px;bottom:8px}
.cert .caption{position:absolute;left:0;right:0;bottom:0;height:24px;background:#6aa9d6;color:#fff;font-size:3.9px;line-height:4.8px;text-align:center;padding:2px 3px}
/* facilities */
.facility-title{position:absolute;left:8px;width:110px;top:52px;text-align:center;font-size:12px;letter-spacing:1.6px;color:var(--blue);line-height:14px}
.facility-info{position:absolute;left:8px;width:110px;top:86px;text-align:center;font-size:5.5px;color:var(--ink);line-height:8px}
.contacts{position:absolute;left:12px;width:104px;top:108px;font-size:4.4px;line-height:6px;color:var(--ink)}
.contacts h4{font-size:5px;font-weight:500;color:var(--blue);letter-spacing:.5px;margin-bottom:1px}
.contacts p{margin-bottom:1.5px}
.contacts b{font-weight:500;color:var(--blue)}
</style>
</head>
<body>

<!-- 1 Cover -->
<section class="slide" style="left:72px;top:23px">
  <svg class="abs" width="313" height="176" viewBox="0 0 313 176" role="img" aria-label="Offshore oil platform at dusk over the sea">
    <defs>
      <linearGradient id="seaSky" x1="0" y1="0" x2="0" y2="1">
        <stop offset="0" stop-color="#5d6670"/>
        <stop offset=".45" stop-color="#8c8f8e"/>
        <stop offset=".62" stop-color="#3f5566"/>
        <stop offset="1" stop-color="#1f3a52"/>
      </linearGradient>
    </defs>
    <polygon points="62,0 313,0 313,176 64,176 151,88" fill="url(#seaSky)"/>
    <polygon points="142,0 198,0 313,140 313,176 286,176" fill="#0692cd" opacity=".55"/>
    <polygon points="62,0 142,0 286,176 64,176 151,88" fill="#0692cd" opacity=".18"/>
    <polygon points="296,0 313,0 313,18" fill="#0692cd"/>
  </svg>
  <div class="brand" style="left:18px;top:58px;font-size:22px;gap:4px"><span class="mark" style="width:26px;height:26px"></span>BRQ</div>
  <div class="cover-tag">A WORLD OF SOLUTIONS</div>
  <div class="cover-title">Business Plan</div>
  <div class="cover-sub">Professional Project, Business<br>and Commercial Template.</div>
</section>

<!-- 2 Agenda -->
<section class="slide" style="left:515px;top:23px">
  <div class="slide-title spaced">Agenda</div>
  <div class="title-rule"></div>
  <div class="brand brand-small"><span class="mark"></span>BRQ</div>

  <div class="agenda-item" style="left:30px;top:40px"><h3>Our Vision, Mission and Goal</h3><p>Where we are heading and how we get there.</p></div>
  <div class="agenda-num" style="left:15px;top:34px">1</div>
  <div class="agenda-item" style="left:176px;top:40px"><h3>Our Journey</h3><p>Since 2011: 50 people, 5 offices in Kuwait, Saudi and UAE.</p></div>
  <div class="agenda-num" style="left:161px;top:34px">2</div>

  <div class="agenda-item" style="left:30px;top:81px"><h3>Our Services</h3><p>Electronics repair &amp; supply, automation projects and brands.</p></div>
  <div class="agenda-num" style="left:15px;top:75px">3</div>
  <div class="agenda-item" style="left:176px;top:81px"><h3>Our Major Client 's</h3><p>Factories, utilities, oil &amp; gas and buildings in Kuwait &amp; Saudi.</p></div>
  <div class="agenda-num" style="left:161px;top:75px">4</div>

  <div class="agenda-item" style="left:30px;top:123px"><h3>Our Facilities</h3><p>Head office, workshops and contacts in three countries.</p></div>
  <div class="agenda-num" style="left:15px;top:117px">5</div>
  <div class="agenda-item" style="left:176px;top:123px"><h3>Certifications &amp; Appreciations</h3><p>Letters of appreciation from the clients we serve.</p></div>
  <div class="agenda-num" style="left:161px;top:117px">6</div>

  <div class="footer">BRQ a World of Solutions</div>
  <div class="page-no">2</div>
</section>

<!-- 3 Vision -->
<section class="slide" style="left:72px;top:218px">
  <div class="slide-title">Our Vision, Mission and Goal</div>
  <div class="title-rule"></div>
  <div class="brand brand-small"><span class="mark"></span>BRQ</div>

  <div class="photo" role="img" aria-label="Photo of a lion" style="left:27px;top:30px;width:58px;height:40px;background:linear-gradient(135deg,#c9a46a,#6d4f2c)"></div>
  <div class="photo" role="img" aria-label="Photo of a glowing light bulb" style="left:27px;top:75px;width:58px;height:40px;background:radial-gradient(circle at 45% 50%,#f3d38a,#6a4a22 70%)"></div>
  <div class="photo" role="img" aria-label="Photo of a row of doors" style="left:27px;top:120px;width:58px;height:40px;background:linear-gradient(180deg,#8a6c4c,#3c2d22)"></div>

  <div class="vm-block" style="top:32px"><h3>VISION</h3><p>To become the leading solution provider in GCC for Industrial Electronic Services,&nbsp; Automation and Energy Efficiency Services</p></div>
  <div class="vm-block" style="top:77px"><h3>MISSION</h3><p>Develop new solutions to mitigate market challenges in Industrial Sector</p></div>
  <div class="vm-block" style="top:122px"><h3>GOAL</h3><p>Offer A One Stop Shop&nbsp; - cost effective solutions for all industrial sector&nbsp; in Controls, Automation and Energy Efficiency Field</p></div>

  <div class="footer">BRQ a World of Solutions</div>
  <div class="page-no">3</div>
</section>

<!-- 4 Journey -->
<section class="slide" style="left:515px;top:218px">
  <div class="slide-title">Our Journey</div>
  <div class="title-rule"></div>

  <svg class="abs" width="313" height="176" viewBox="0 0 313 176">
    <g fill="none" stroke="#0692cd" stroke-width="1">
      <polyline points="47,45 60,45 60,83 176,83"/>
      <polyline points="82,104 86,104 86,92 176,92"/>
      <polyline points="126,95 176,95"/>
      <polyline points="120,130 120,98 176,98"/>
      <polyline points="145,132 145,102 176,102"/>
      <polyline points="168,118 168,106 176,106"/>
    </g>
    <g fill="#0692cd">
      <circle cx="47" cy="45" r="1.6"/><circle cx="60" cy="83" r="1.6"/><circle cx="82" cy="104" r="1.6"/>
      <circle cx="126" cy="95" r="1.6"/><circle cx="120" cy="130" r="1.6"/><circle cx="145" cy="132" r="1.6"/><circle cx="168" cy="118" r="1.6"/>
    </g>
    <circle cx="109" cy="52" r="6" fill="#8fa3b3" role="img" aria-label="Fund emblem"/>
  </svg>

  <div class="year" style="left:22px;top:41px">2012<small>Repairing<br>Industrial<br>Electronics</small></div>
  <div class="year" style="left:24px;top:75px;text-align:right;width:32px"><small>Field<br>Maintenance -<br>AMC</small></div>
  <div class="year" style="left:52px;top:100px;text-align:center">2013<small>Automation<br>Solutions</small></div>
  <div class="year" style="left:95px;top:98px;text-align:center">2015<small>Dammam<br>(KSA)<br>Established</small></div>
  <div class="year" style="left:78px;top:133px;text-align:center">2014<small>Riyadh (KSA)<br>Established</small></div>
  <div class="year" style="left:130px;top:136px;text-align:center">2017<small>Energy<br>Monitoring<br>Solutions</small></div>
  <div class="year" style="left:174px;top:120px">2018<small>Smart<br>Control<br>Solutions</small></div>

  <div class="journey-note">BRQ is a Coastal Venture Fund supported company, till date provided&nbsp; services to 30,000 Industrial electronic equipment's and supported&nbsp; 2,000 clients in Kuwait and Saudi.</div>
  <div class="brand brand-large"><span class="mark"></span>BRQ</div>
  <div class="brand-large-tag">A WORLD OF SOLUTIONS</div>

  <div class="footer">BRQ a World of Solutions</div>
  <div class="page-no">4</div>
</section>

<!-- 5 Services hub -->
<section class="slide" style="left:72px;top:414px">
  <svg class="abs" width="313" height="176" viewBox="0 0 313 176" role="img" aria-label="Offshore platform under a stormy teal sky">
    <defs>
      <linearGradient id="stormy" x1="0" y1="0" x2="0" y2="1">
        <stop offset="0" stop-color="#2c4754"/>
        <stop offset=".5" stop-color="#4f7381"/>
        <stop offset="1" stop-color="#1c3340"/>
      </linearGradient>
    </defs>
    <rect width="313" height="176" fill="url(#stormy)"/>
    <circle cx="64" cy="79" r="48" fill="#8fc4da" opacity=".28"/>
    <circle cx="64" cy="79" r="37" fill="#5aa8cf" opacity=".55"/>
    <g fill="none" stroke="rgba(255,255,255,.75)" stroke-width=".8">
      <path d="M91,34 A48,48 0 0 1 91,139"/>
      <line x1="91" y1="34" x2="161" y2="34"/>
      <line x1="118" y1="53" x2="161" y2="53"/>
      <line x1="128" y1="87" x2="161" y2="87"/>
      <line x1="118" y1="119" x2="161" y2="119"/>
      <line x1="91" y1="139" x2="161" y2="139"/>
    </g>
    <g fill="#2c4754" stroke="#fff" stroke-width="1.2">
      <circle cx="91" cy="34" r="3"/><circle cx="118" cy="53" r="3"/><circle cx="128" cy="87" r="3"/><circle cx="118" cy="119" r="3"/><circle cx="91" cy="139" r="3"/>
    </g>
  </svg>
  <div class="abs" style="left:40px;top:68px;font-size:9.5px;color:#fff">Our Services</div>
  <div class="brand" style="left:43px;top:80px;font-size:17px;color:#fff;gap:3px"><span class="mark" style="width:8px;height:8px;background:#fff"></span>BRQ</div>

  <div class="hub-pill" style="top:26px">ENERGY EFFICIENCY<br>SERVICES</div>
  <div class="hub-pill" style="top:47px">INDUSTRIAL<br>AUTOMATION</div>
  <div class="hub-pill" style="top:80px">INDUSTRIAL ANNUAL<br>MAINTENANCE</div>
  <div class="hub-pill" style="top:111px">EMERGENCY<br>SERVICES</div>
  <div class="hub-pill" style="top:131px">INDUSTRIAL<br>REPAIR</div>

  <div class="footer hub-footer">BRQ a World of Solutions</div>
  <div class="page-no" style="color:#fff;border:0">5</div>
</section>

<!-- 6 Repair & supply / automation -->
<section class="slide" style="left:515px;top:414px">
  <div class="slide-title spaced">Our Services (Cont.)</div>
  <div class="title-rule"></div>
  <div class="brand brand-small"><span class="mark"></span>BRQ</div>

  <div class="photo" role="img" aria-label="Industrial plant by the sea at dusk" style="left:27px;top:31px;width:113px;height:68px;background:linear-gradient(180deg,#6fa3c9,#3b5f7c 60%,#d69a5b)"></div>
  <div class="photo" role="img" aria-label="Control room with large screen wall" style="left:172px;top:31px;width:113px;height:68px;background:linear-gradient(180deg,#2d3b3d,#3fbfb5 40%,#dfe7ea 75%)"></div>

  <div class="card-head" style="left:27px;top:106px">Industrial Electronics Repair &amp; Supply</div>
  <ol class="card-list" style="left:27px;top:113px">
    <li><span>1.</span>Power supplies and secondary DC supplies</li>
    <li><span>2.</span>Processor, memory, analog and digital I/O cards</li>
    <li><span>3.</span>Communication cards, remote I/O, PCB boards</li>
    <li><span>4.</span>PLCs, drives, servo drives, inverters, HMIs</li>
    <li><span>5.</span>Industrial monitors and operator interfaces</li>
    <li><span>6.</span>Wire feeders, weld timers and robot arms</li>
  </ol>
  <div class="card-head" style="left:178px;top:106px;letter-spacing:.8px">Automation Solutions</div>
  <ol class="card-list" style="left:172px;top:113px">
    <li><span>1.</span>PLC and DCS design and programming</li>
    <li><span>2.</span>SCADA and HMI development</li>
    <li><span>3.</span>Drive and motion control systems</li>
    <li><span>4.</span>Plant upgrades and control retrofits</li>
    <li><span>5.</span>Site commissioning and support</li>
  </ol>

  <div class="footer">BRQ a World of Solutions</div>
  <div class="page-no">6</div>
</section>

<!-- 7 Repairing -->
<section class="slide" style="left:72px;top:610px">
  <div class="slide-title">Our Services (Cont.)</div>
  <div class="title-rule"></div>
  <div class="brand brand-small"><span class="mark"></span>BRQ</div>

  <div class="photo" role="img" aria-label="Repair workshop with control panels and monitors" style="left:14px;top:35px;width:134px;height:106px;background:linear-gradient(180deg,#c65a4e 0%,#d9dcdf 35%,#9fb6c6 70%,#e9ecef)"></div>

  <div class="repair-title">Repairing of Industrial<br>Panels and Equipment</div>
  <ol class="repair-list">
    <li>1.&nbsp; Induction heater</li>
    <li>2.&nbsp; Brazing Machine</li>
    <li>3.&nbsp; High voltaje plasma generator</li>
    <li>4.&nbsp; High current rectifier panels</li>
    <li>5.&nbsp; PLC and DCS panels</li>
    <li>6.&nbsp; ATS and AMF panels</li>
    <li>7.&nbsp; APFC Panels</li>
    <li>8.&nbsp; Fire Fighting control panels</li>
    <li>9.&nbsp; CNC Machine Control panels</li>
    <li>10.UPS and inverters</li>
  </ol>

  <div class="footer">BRQ a World of Solutions</div>
  <div class="page-no">7</div>
</section>

<!-- 8 Projects & brands -->
<section class="slide" style="left:515px;top:610px">
  <div class="slide-title">Our Services (Cont.)</div>
  <div class="title-rule"></div>
  <div class="brand brand-small"><span class="mark"></span>BRQ</div>

  <div class="photo" role="img" aria-label="Operator desk with many process screens" style="left:27px;top:31px;width:113px;height:68px;background:linear-gradient(180deg,#24475f,#2f6f94 50%,#1a2228)"></div>
  <div class="photo" role="img" aria-label="Control room monitoring screens" style="left:172px;top:31px;width:113px;height:68px;background:linear-gradient(180deg,#1d5f93,#3a8dc4 55%,#2b3d4b)"></div>

  <div class="card-head" style="left:27px;top:106px">Automation Projects</div>
  <ol class="card-list" style="left:27px;top:113px">
    <li><span>1.</span>Water pumping station PLC upgrade, Kuwait</li>
    <li><span>2.</span>Steel mill drive retrofit, Dammam</li>
    <li><span>3.</span>Packing line SCADA system, UAE</li>
    <li><span>4.</span>Wastewater plant control panels, Riyadh</li>
    <li><span>5.</span>Mall building management integration</li>
    <li><span>6.</span>Stadium energy monitoring system</li>
  </ol>
  <div class="card-head" style="left:178px;top:106px;letter-spacing:.8px">Major Brands We Support</div>
  <ol class="card-list" style="left:172px;top:113px">
    <li><span>1.</span>Voltrex &ndash; PLCs, I/O and remote I/O</li>
    <li><span>2.</span>Ardenne Controls &ndash; HMIs and panels</li>
    <li><span>3.</span>Mirokai Drives &ndash; servo drives, motors</li>
    <li><span>4.</span>Kestrel Automation &ndash; robots, welders</li>
    <li><span>5.</span>Our value: QFP &ndash; Quality, Fast, Price</li>
  </ol>

  <div class="footer">BRQ a World of Solutions</div>
  <div class="page-no">8</div>
</section>

<!-- 9 Energy efficiency -->
<section class="slide" style="left:72px;top:805px">
  <div class="slide-title">Our Services</div>
  <div class="title-rule"></div>
  <div class="brand brand-small"><span class="mark"></span>BRQ</div>

  <div class="energy-title">ENERGY<br>EFFICIENCY<br>SERVICES<br><small>(Monitoring &amp;<br>Controlling)</small></div>
  <ul class="energy-list">
    <li>-&nbsp; Industries</li>
    <li>-&nbsp; Office Buildings</li>
    <li>-&nbsp; Commercial Buildings</li>
    <li>-&nbsp; Schools</li>
    <li>-&nbsp; Universities</li>
  </ul>

  <div class="photo" role="img" aria-label="Diagram of a solar power management system with gateways, meters and sensors" style="left:115px;top:29px;width:187px;height:136px;border-radius:14px;background:linear-gradient(180deg,#e4e7ea 0%,#e4e7ea 40%,#f4f6f8 40%,#eef1f4);box-shadow:0 2px 6px rgba(0,0,0,.2)"></div>

  <div class="footer">BRQ a World of Solutions</div>
</section>

<!-- 10 Clients -->
<section class="slide" style="left:515px;top:805px">
  <div class="slide-title">Our Major Clients – Kuwait &amp; Saudi</div>
  <div class="title-rule"></div>
  <div class="brand brand-small"><span class="mark"></span>BRQ</div>

  <div class="abs" role="img" aria-label="Map of Kuwait" style="left:14px;top:56px;width:75px;height:76px;border-radius:30% 45% 40% 25%;background:linear-gradient(135deg,#a9acae,#8d9093)"></div>

  <div class="client" style="left:138px;top:50px"><i></i>Meridian Drilling</div>
  <div class="client" style="left:184px;top:50px">Halvern Drilling</div>
  <div class="client" style="left:233px;top:50px">Stormgate</div>
  <div class="client" style="left:276px;top:50px">Bayline Drill Co.</div>

  <div class="client" style="left:138px;top:80px">Ostra</div>
  <div class="client" style="left:184px;top:80px">Carrowmere</div>
  <div class="client" style="left:233px;top:80px">HRF</div>
  <div class="client" style="left:276px;top:80px">Pelmar</div>

  <div class="client" style="left:138px;top:112px">GWTR</div>
  <div class="client" style="left:184px;top:112px">Olvar</div>
  <div class="client" style="left:233px;top:112px">BZA</div>
  <div class="client" style="left:276px;top:112px">PAV</div>

  <div class="client" style="left:184px;top:142px">DRH</div>
  <div class="client" style="left:233px;top:142px">Kellmont</div>

  <div class="footer">BRQ a World of Solutions</div>
  <div class="page-no">10</div>
</section>

<!-- 11 Certification -->
<section class="slide" style="left:72px;top:1001px">
  <div class="slide-title">Certification and Appreciations</div>
  <div class="title-rule"></div>
  <div class="brand brand-small"><span class="mark"></span>BRQ</div>

  <div class="cert" style="left:11px">
    <div class="sheet"><b style="top:14px;right:30px"></b><b style="top:24px"></b><b style="top:28px"></b><b style="top:32px"></b><b style="top:36px"></b><b style="top:44px"></b><b style="top:48px"></b><b style="top:56px;right:34px"></b><div class="seal"></div></div>
    <div class="caption">Alloyra Steel &ndash; appreciation for drive and PLC card repairs.</div>
  </div>
  <div class="cert" style="left:84px">
    <div class="sheet"><b style="top:12px;left:40px"></b><b style="top:22px"></b><b style="top:28px"></b><b style="top:32px"></b><b style="top:36px"></b><b style="top:42px"></b><b style="top:46px"></b><b style="top:60px;right:34px"></b><div class="seal" style="left:auto;right:8px"></div></div>
    <div class="caption">HRF &ndash; appreciation for field maintenance and fast support.</div>
  </div>
  <div class="cert" style="left:158px">
    <div class="sheet"><b style="top:12px;right:36px"></b><b style="top:20px"></b><b style="top:26px"></b><b style="top:30px"></b><b style="top:34px"></b><b style="top:40px"></b><b style="top:52px;right:30px"></b><div class="seal" style="left:26px"></div></div>
    <div class="caption">Tabela Foods &ndash; appreciation for packing line automation.</div>
  </div>
  <div class="cert" style="left:230px">
    <div class="sheet"><b style="top:12px;left:22px"></b><b style="top:22px"></b><b style="top:26px"></b><b style="top:30px"></b><b style="top:34px"></b><b style="top:40px"></b><b style="top:44px"></b><b style="top:54px;right:34px"></b><div class="seal" style="left:22px;bottom:26px"></div></div>
    <div class="caption">Binaa Engineering &ndash; appreciation for control panel works.</div>
  </div>

  <div class="footer">BRQ a World of Solutions</div>
  <div class="page-no">11</div>
</section>

<!-- 12 Facilities & contacts -->
<section class="slide" style="left:515px;top:1001px">
  <div class="brand" style="left:16px;top:7px;font-size:10px"><span class="mark" style="width:10px;height:10px"></span>BRQ</div>
  <div class="facility-title">Our Facilitys<br>Kuwait</div>
  <div class="facility-info">BRQ Company (Head Office)<br>Total Area # 300 m2</div>
  <div class="contacts">
    <h4>CONTACT US</h4>
    <p><b>Kuwait</b> &nbsp;+965 5550 1100</p>
    <p><b>Saudi</b> &nbsp;Riyadh &amp; Dammam +966 5550 2200</p>
    <p><b>UAE</b> &nbsp;+971 5550 3300</p>
    <p>info@brq-company.example</p>
  </div>

  <div class="abs" role="img" aria-label="Office workstations" style="left:126px;top:0;width:92px;height:86px;background:linear-gradient(180deg,#e7eaee,#c9cfd6 60%,#9aa6b2)"></div>
  <div class="abs" role="img" aria-label="Technicians at repair benches" style="left:220px;top:0;width:93px;height:86px;background:linear-gradient(180deg,#cfd5da,#8e9aa6 55%,#5d6f80)"></div>
  <div class="abs" role="img" aria-label="Electronics test bench with equipment" style="left:126px;top:88px;width:92px;height:88px;background:linear-gradient(180deg,#d7dde2,#9aa5b0 60%,#6a7784)"></div>
  <div class="abs" role="img" aria-label="Close-up of an industrial operator panel" style="left:220px;top:88px;width:93px;height:88px;background:linear-gradient(135deg,#2f4fa3,#1a2f6a 60%,#4a5870)"></div>
</section>

</body>
</html>
```